Business Card Design Project - bel soravin group

dear Sirs

we need business card design for our group ( BEL Soravin Group ) , i have got the Logo design of our group from pixel harbor in previous , so all need details relating to our group i think available with you, as well as the the chosen logo design

we hope to provide us with business card logo that to be appropaite and satisfactory to us .

thanks

note : logo design of our group is attached .
Updates

Reason: please extend the deadline of my project for additional 15 days because i didn't received appropriate design for our gruop yet . kindly beaware that i have received 77 design till now , supossed to send me 200-250 design at least . thanks

Target Market(s)

contents
-

name : Korvan EL Mistrani

position : Operation Manager

Industry/Entity Type

Business

Requirements
Must have

• person name

group logo
Nice to have
• logo color matching with back background

```html
<!DOCTYPE html>
<html lang="en">
<head>
<meta charset="utf-8">
<title>BEL Soravin Group – Business Cards</title>
<link rel="stylesheet" href="https://fonts.googleapis.com/css2?family=Questrial&family=Arimo:wght@400;700&display=swap">
<style>
  :root {
    --stage: #e6e8eb;
    --card-white: #ffffff;
    --card-mist: #eef0f3;
    --brand-blue: #1a4f93;
    --brand-blue-deep: #143f78;
    --ink: #222831;
    --on-blue: #ffffff;
    --on-blue-soft: #dbe5f3;
  }
  * { box-sizing: border-box; margin: 0; padding: 0; }
  html, body {
    width: 1200px; height: 900px; overflow: hidden;
    background: var(--stage);
  }
  .stage {
    position: relative; width: 1200px; height: 900px;
    display: flex; align-items: center; justify-content: center; gap: 40px;
  }
  .card {
    position: relative; width: 540px; height: 309px; overflow: hidden;
    border-radius: 4px;
    background: linear-gradient(135deg, var(--card-white) 0%, var(--card-mist) 100%);
    box-shadow: 0 10px 30px rgba(20, 30, 50, 0.18);
  }

  /* brand name lockup */
  .brand {
    display: flex; align-items: center; gap: 12px;
    font-family: "Questrial", sans-serif; color: var(--brand-blue);
    text-transform: uppercase; letter-spacing: 1px; line-height: 1;
  }
  .brand__mark { background: var(--brand-blue); flex: none; }

  /* front */
  .card--front {
    display: flex; flex-direction: column; align-items: center; justify-content: center; gap: 34px;
  }
  .card--front .brand { font-size: 42px; }
  .card--front .brand__mark { width: 20px; height: 20px; }
  .front__web {
    font-family: "Arimo", sans-serif; font-size: 15px; letter-spacing: 2px; color: var(--ink);
  }

  /* back */
  .back__top { position: absolute; left: 0; right: 0; top: 0; height: 132px; }
  .card--back .brand {
    position: absolute; right: 34px; top: 48px; font-size: 30px;
  }
  .card--back .brand__mark { width: 14px; height: 14px; }
  .back__band {
    position: absolute; left: 0; right: 0; top: 132px; bottom: 0;
    background: linear-gradient(180deg, var(--brand-blue) 0%, var(--brand-blue-deep) 100%);
    color: var(--on-blue); font-family: "Arimo", sans-serif;
    padding: 22px 30px 0 36px; display: flex; justify-content: space-between;
  }
  .back__band::before {
    content: ""; position: absolute; left: 56px; top: -12px;
    border-left: 12px solid transparent; border-right: 12px solid transparent;
    border-bottom: 12px solid var(--brand-blue);
  }
  .person__name { font-size: 17px; font-weight: 700; }
  .person__role { font-size: 12px; color: var(--on-blue-soft); margin-top: 4px; }
  .person__address { font-size: 12px; line-height: 1.45; margin-top: 16px; color: var(--on-blue-soft); }
  .contacts { list-style: none; font-size: 12px; padding-top: 34px; }
  .contacts li { display: flex; align-items: center; gap: 9px; height: 19px; }
  .contacts svg { width: 12px; height: 12px; fill: var(--on-blue); flex: none; }
</style>
</head>
<body>
<main class="stage">

  <section class="card card--front" aria-label="Card front">
    <div class="brand"><span class="brand__mark"></span><span class="brand__name">BEL Soravin Group</span></div>
    <p class="front__web">www.belsoravingroup.com</p>
  </section>

  <section class="card card--back" aria-label="Card back">
    <div class="back__top">
      <div class="brand"><span class="brand__mark"></span><span class="brand__name">BEL Soravin Group</span></div>
    </div>
    <div class="back__band">
      <div class="person">
        <p class="person__name">Korvan EL Mistrani</p>
        <p class="person__role">Operation Manager</p>
        <p class="person__address">Marvel Crest Area - Section 412<br>Street 7 - Building 33<br>Halvora - Norland</p>
      </div>
      <ul class="contacts">
        <li><svg viewBox="0 0 24 24"><path d="M6.6 10.8a15 15 0 0 0 6.6 6.6l2.2-2.2c.3-.3.7-.4 1-.2 1.1.4 2.3.6 3.6.6.6 0 1 .4 1 1V20c0 .6-.4 1-1 1A17 17 0 0 1 3 4c0-.6.4-1 1-1h3.5c.6 0 1 .4 1 1 0 1.3.2 2.5.6 3.6.1.3 0 .7-.2 1z"/></svg>+971 550 0004418</li>
        <li><svg viewBox="0 0 24 24"><path d="M7 1h10a2 2 0 0 1 2 2v18a2 2 0 0 1-2 2H7a2 2 0 0 1-2-2V3a2 2 0 0 1 2-2zm0 3v14h10V4zm5 15.5a1 1 0 1 0 0 2 1 1 0 0 0 0-2z"/></svg>+971-550-7777315</li>
        <li><svg viewBox="0 0 24 24"><path d="M6 2h10l2 2v4H6zM4 9h16a2 2 0 0 1 2 2v7h-4v4H6v-4H2v-7a2 2 0 0 1 2-2zm4 7v4h8v-4z"/></svg>+ 000 000 1111111</li>
        <li><svg viewBox="0 0 24 24"><path d="M2 5h20v14H2zm2 2v.5l8 5 8-5V7zm0 2.8V17h16V9.8l-8 5z"/></svg>info@belsoravingroup.com</li>
        <li><svg viewBox="0 0 24 24"><path d="M12 2a10 10 0 1 0 0 20 10 10 0 0 0 0-20zm0 2c.9 0 2.2 1.9 2.7 5H9.3C9.8 5.9 11.1 4 12 4zM4.3 11h3a17 17 0 0 0 .2 2h-3.2a8 8 0 0 1 0-2zm5 0h5.4a15 15 0 0 1 0 2H9.3a15 15 0 0 1 0-2zm7.4 0h3a8 8 0 0 1 0 2h-3.2a17 17 0 0 0 .2-2zM9.3 15h5.4c-.5 3.1-1.8 5-2.7 5s-2.2-1.9-2.7-5z"/></svg>www.belsoravingroup.com</li>
      </ul>
    </div>
  </section>

</main>
</body>
</html>
```